Garnett and Lyle Personal Injury Billboard

We'd like a clean/modern billboard to build brand awareness for our law firm in the area of personal injury. Ideally, we like the word "Injured?" or something similar in large lettering.

I'm attaching images, logo and award badges which could be used. The billboards will be 14x48 ft and 10.6x36.

We are open to different color ideas, fonts, and artwork. Creative but not too busy with wording. Our web page is www.kgarnettfirm.example

Garnett & Lyle Law Firm
(555) 318-4092

```html
<!DOCTYPE html>
<html lang="en">
<head>
<meta charset="UTF-8">
<title>Garnett &amp; Lyle Law Firm — Injury Billboard</title>
<link rel="stylesheet" href="https://fonts.googleapis.com/css2?family=Lilita+One&family=Montserrat:wght@400;500;700&display=swap">
<style>
  :root {
    --page-bg: #ffffff;
    --navy: #0b1f48;
    --mid-blue: #0a4c9e;
    --bright-blue: #0b8bc6;
    --accent-blue: #1fa3e3;
    --white: #ffffff;
    --suit-grey: #6c7079;
    --suit-dark: #3f4656;
  }
  * { margin: 0; padding: 0; box-sizing: border-box; }
  html, body {
    width: 1138px;
    height: 1200px;
    overflow: hidden;
    background: var(--page-bg);
  }
  .billboard {
    position: absolute;
    left: 54px;
    top: 450px;
    width: 1030px;
    height: 300px;
    overflow: hidden;
    background: var(--navy);
  }
  .billboard__bands {
    position: absolute;
    inset: 0;
    width: 100%;
    height: 100%;
  }
  .headline {
    position: absolute;
    left: 43px;
    top: 52px;
    font-family: "Lilita One", sans-serif;
    font-weight: 400;
    font-size: 82px;
    line-height: 1;
    color: var(--white);
    letter-spacing: 1px;
    white-space: nowrap;
  }
  .callout {
    position: absolute;
    left: 43px;
    top: 132px;
    font-family: "Montserrat", sans-serif;
    font-weight: 500;
    font-size: 45px;
    line-height: 1;
    color: var(--accent-blue);
    white-space: nowrap;
  }
  .phone {
    position: absolute;
    left: 42px;
    top: 182px;
    font-family: "Montserrat", sans-serif;
    font-weight: 700;
    font-size: 50px;
    line-height: 1;
    color: var(--white);
    letter-spacing: -1px;
    white-space: nowrap;
  }
  .offer {
    position: absolute;
    left: 101px;
    top: 246px;
    font-family: "Montserrat", sans-serif;
    font-weight: 500;
    font-size: 16px;
    letter-spacing: 2.8px;
    color: var(--white);
    white-space: nowrap;
  }
  .attorney-photo {
    position: absolute;
    left: 420px;
    top: 0;
    width: 300px;
    height: 300px;
    background: linear-gradient(160deg, rgba(63,70,86,0) 0%, var(--suit-dark) 30%, var(--suit-grey) 70%, var(--suit-dark) 100%);
    border-radius: 110px 110px 0 0;
  }
  .firm-name {
    position: absolute;
    left: 740px;
    top: 96px;
    width: 240px;
    font-family: "Montserrat", sans-serif;
    font-weight: 700;
    font-size: 36px;
    line-height: 1.1;
    color: var(--white);
    white-space: nowrap;
  }
  .firm-name__line { display: block; }
</style>
</head>
<body>
  <section class="billboard" aria-label="Garnett &amp; Lyle Law Firm personal injury billboard">
    <svg class="billboard__bands" viewBox="0 0 1030 300" preserveAspectRatio="none" aria-hidden="true">
      <rect width="1030" height="300" fill="var(--navy)"/>
      <polygon points="575,0 1030,0 1030,300 308,300" fill="var(--mid-blue)"/>
      <polygon points="933,0 1030,0 1030,300 675,300" fill="var(--bright-blue)"/>
    </svg>

    <h1 class="headline">INJURED?</h1>
    <p class="callout">CALL US TODAY</p>
    <p class="phone">(555) 318-4092</p>
    <p class="offer">FREE CASE EVALUATION</p>

    <div class="attorney-photo" role="img" aria-label="Photograph of the firm's two attorneys in suits, smiling"></div>

    <p class="firm-name">
      <span class="firm-name__line">Garnett</span>
      <span class="firm-name__line">&amp; Lyle</span>
      <span class="firm-name__line">Law Firm</span>
    </p>
  </section>
</body>
</html>
```